Harbourline Works Group Business Card Redesign

Logo has already been developed. The current business card is one sided. We'd like our mission on the back and more creativity so it pops. We may also like a tagline on the back
One call...all the service, all the savings. Examples are attached from our printer but we don't like them. The front is how we have our existing cards but the back is new. We are open to all ideas. We do like our colors/ brand of purple, black, white...

```html
<!DOCTYPE html>
<html lang="en">
<head>
<meta charset="utf-8">
<title>Harbourline Works Group – Business Card</title>
<link rel="stylesheet" href="https://fonts.googleapis.com/css2?family=Ubuntu:ital,wght@0,500;0,700;1,500;1,700&family=Roboto:wght@500;700&family=EB+Garamond:wght@400;700&display=swap">
<style>
  :root {
    --brand-purple: #7d0b73;
    --brand-purple-deep: #66075e;
    --ink: #141414;
    --paper: #f4f3f1;
    --backdrop: #cfcfcf;
  }
  * { box-sizing: border-box; margin: 0; padding: 0; }
  html, body { width: 1200px; height: 1000px; overflow: hidden; }
  body {
    background: var(--backdrop);
    display: flex;
    flex-direction: column;
    align-items: center;
    justify-content: center;
    gap: 60px;
  }
  .card {
    position: relative;
    width: 600px;
    height: 343px;
    background: var(--paper);
    overflow: hidden;
    box-shadow: 0 4px 14px rgba(0,0,0,0.18);
  }

  /* Back side */
  .card-back__panel {
    position: absolute;
    inset: 0;
    background: linear-gradient(135deg, var(--brand-purple-deep), var(--brand-purple));
    clip-path: polygon(0 0, 72% 0, 44% 100%, 0 100%);
  }
  .mission {
    position: absolute;
    left: 40px;
    top: 42px;
    width: 250px;
    color: #fff;
    font-family: "Ubuntu", sans-serif;
    font-style: italic;
  }
  .mission__title { font-weight: 700; font-size: 19px; margin-bottom: 2px; }
  .mission__text { font-weight: 500; font-size: 14.5px; line-height: 1.25; }
  .tagline {
    position: absolute;
    right: 34px;
    bottom: 40px;
    text-align: right;
    color: var(--brand-purple);
    font-family: "Ubuntu", sans-serif;
    font-weight: 700;
    font-style: italic;
    font-size: 24px;
    line-height: 1.15;
  }

  /* Front side */
  .brand {
    position: absolute;
    left: 30px;
    top: 34px;
    display: flex;
    align-items: center;
    gap: 16px;
  }
  .brand__dot {
    flex: none;
    width: 56px; height: 56px;
    border-radius: 50%;
    background: var(--brand-purple);
  }
  .company { font-family: "Roboto", sans-serif; }
  .company__name { color: var(--brand-purple); font-weight: 500; font-size: 27px; line-height: 1.1; }
  .company__slogan { color: var(--ink); font-weight: 700; font-size: 17.5px; margin-top: 2px; }
  .contact { font-family: "EB Garamond", serif; color: var(--ink); }
  .person {
    position: absolute;
    left: 0; right: 0;
    top: 140px;
    text-align: center;
  }
  .person__name { font-weight: 700; font-size: 19px; }
  .person__title { font-size: 15px; }
  .address {
    position: absolute;
    left: 30px;
    top: 200px;
    font-size: 15px;
    line-height: 1.3;
    font-style: normal;
    color: #333;
  }
  .phones {
    position: absolute;
    right: 30px;
    top: 202px;
    text-align: right;
    font-size: 15.5px;
    line-height: 1.3;
  }
  .email {
    position: absolute;
    right: 30px;
    top: 272px;
    font-size: 15px;
  }
  .card-front__band {
    position: absolute;
    left: 0; right: 0;
    bottom: 12px;
    height: 14px;
    background: var(--brand-purple);
  }
</style>
</head>
<body>

  <section class="card card-back" aria-label="Card back">
    <div class="card-back__panel"></div>
    <div class="mission">
      <h2 class="mission__title">Our Mission</h2>
      <p class="mission__text">To ensure the injured worker returns to function and work, faster, better, stronger while creating longterm client loyalty through service and value we provide.</p>
    </div>
    <p class="tagline">One Call -<br>All the Service<br>All the Savings</p>
  </section>

  <section class="card card-front" aria-label="Card front">
    <div class="brand">
      <span class="brand__dot"></span>
      <div class="company">
        <h1 class="company__name">Harbourline Works Group</h1>
        <p class="company__slogan">Delivering Results. Creating Savings.</p>
      </div>
    </div>
    <div class="contact person">
      <p class="person__name">Dana Whitfield</p>
      <p class="person__title">Business Development Manager</p>
    </div>
    <address class="contact address">
      4180 Cedar Ridge Road<br>Suite 210<br>Tempe, AZ 85281
    </address>
    <div class="contact phones">
      <p>Main : (555) 014-2200</p>
      <p>Fax : (555) 014-2201</p>
      <p>Cell : (555) 014-3377</p>
    </div>
    <p class="contact email">e-mail: dwhitfield@HarbourlineWorksGroup.com</p>
    <div class="card-front__band"></div>
  </section>

</body>
</html>
```